Toll For Safer Streets

We need web design for an anti-gun violence campaign that will urge people to ring bells instead of shooting guns to bring in the New Year and whenever someone is killed by gun violence.
This campaign will raise funds for social agencies that help communities with social issues to help especially youth with no place to turn, play or dream. Also will fund New Gun Laws policies. Should be global in aspect but appealing to United States first.
Find poem by Lord Edmund Halvercombe "Turn Lamps, Pale Lamps" as our theme on google.
This is a start up and nothing else to give. But need something eye catching for appeal of campaign.

Target Market(s)

Universal , more male oriented.

Industry/Entity Type

Gun

Number of Pages Required

1 page

Other font styles liked:
• Designers Can Choose

Requirements
Must have
• Strong imagery and vivid colors and bell of course.
Nice to have
• A stand out design beyond words that hit home. See attached file for website ideas

```html
<!DOCTYPE html>
<html lang="en">
<head>
<meta charset="utf-8">
<title>Toll For Safer Streets</title>
<link href="https://fonts.googleapis.com/css2?family=Mulish:ital,wght@0,400;0,500;0,600;0,700;1,400&display=swap" rel="stylesheet">
<style>
:root{
  --pink:#d8174a;
  --text:#3d3d3d;
  --muted:#6b6b6b;
  --line:#e4e4e4;
  --panel:#f7f7f7;
  --footer:#3a3a3a;
}
*{box-sizing:border-box;margin:0;padding:0}
html,body{width:910px;height:1200px;overflow:hidden;background:#fff}
body{position:relative;font-family:"Mulish",sans-serif;color:var(--text)}
.abs{position:absolute}

/* header */
.brand{left:56px;top:32px;display:flex;gap:6px;align-items:flex-start}
.brand-mark{width:46px;height:46px;background:var(--pink)}
.brand-name{font-size:10px;line-height:11.5px;font-weight:600;color:#555}
.top-donate{left:739px;top:10px;width:116px;height:22px;background:var(--pink);color:#fff;font-size:9.5px;font-weight:600;display:flex;align-items:center;justify-content:center;letter-spacing:.2px}
.nav{left:256px;top:67px;width:599px;display:flex;justify-content:space-between;font-size:8.6px;font-weight:500;color:#444}
.nav a{color:inherit;text-decoration:none;padding:0 10px 8px;position:relative}
.nav a:last-child{padding-right:0}
.nav a.current{color:var(--pink)}
.nav a.current::after{content:"";position:absolute;left:0;right:0;bottom:0;height:2.5px;background:var(--pink)}

/* hero */
.hero{left:0;top:94px;width:910px;height:299px;background:linear-gradient(90deg,#050505 0%,#0c0c0c 15%,#161616 50%,#2c2c2e 82%,#0e0e0e 100%)}
.hero-photo{position:absolute;left:142px;top:0;width:314px;height:299px;
  clip-path:polygon(3% 0,97% 0,99% 20%,96% 42%,99% 66%,97% 100%,8% 100%,4% 78%,1% 52%,5% 28%,0 10%);
  background:
    radial-gradient(ellipse 60% 22% at 30% 72%,rgba(255,236,196,.9),rgba(255,236,196,0) 70%),
    radial-gradient(ellipse 55% 18% at 72% 50%,rgba(255,226,170,.85),rgba(255,226,170,0) 70%),
    linear-gradient(180deg,#b8aaa4 0%,#d6b08a 30%,#eab67a 55%,#e49a5e 78%,#8a5a3c 100%)}
.quote{position:absolute;left:498px;top:96px;font-size:22.5px;line-height:30px;font-style:italic;color:#fff;white-space:nowrap}
.qmark{position:absolute;font-size:40px;font-weight:700;color:#5c5c5c;font-style:normal;line-height:1}
.author{position:absolute;left:498px;top:190px;font-size:13px;font-weight:600;color:var(--pink)}
.arrows{position:absolute;left:808px;top:250px}

/* donation */
.donate-box{left:56px;top:422px;width:798px;height:76px;background:var(--panel);border:1px solid var(--line);box-shadow:0 10px 8px -8px rgba(0,0,0,.25)}
.donate-title{position:absolute;left:114px;top:11px;font-size:23px;font-weight:500;color:var(--pink);letter-spacing:.3px}
.donate-sub{position:absolute;left:116px;top:41px;font-size:18px;color:#3c3c3c}
.donate-btn{position:absolute;left:621px;top:15px;width:157px;height:45px;background:var(--pink);color:#fff;font-size:18.5px;font-weight:600;display:flex;align-items:center;justify-content:center}

/* feature cards */
.card{top:526px;width:250px;height:282px;background:var(--panel);border:1px solid var(--line);border-top:3px solid var(--pink);box-shadow:0 10px 8px -8px rgba(0,0,0,.22)}
.card-img{position:absolute;left:14px;top:14px;width:222px;height:124px}
.card-title{position:absolute;left:14px;top:150px;font-size:14.5px;font-weight:500;color:#333}
.card-title em{font-style:normal;color:var(--pink)}
.card-text{position:absolute;left:14px;top:174px;width:215px;font-size:9.4px;line-height:16px;color:#555}
.card-link{position:absolute;left:13px;top:252px;font-size:9.4px;color:var(--pink)}

/* blog */
.rule{left:56px;top:842px;width:798px;height:1px;background:var(--line)}
.blog-head{left:56px;top:860px;font-size:14.5px;font-weight:500;color:#333}
.blog-head em{font-style:normal;color:var(--pink)}
.post{top:894px;width:186px}
.post-img{width:184px;height:105px}
.post-title{margin-top:12px;font-size:11px;font-weight:500;color:var(--pink);white-space:nowrap}
.post-date{margin-top:4px;font-size:8px;font-style:italic;color:#999}
.post-text{margin-top:4px;width:176px;font-size:9.2px;line-height:14px;color:#555}

/* footer */
.footer{left:0;top:1118px;width:910px;height:82px;background:var(--footer)}
.foot-brand{position:absolute;left:56px;top:16px;display:flex;gap:5px}
.foot-mark{width:34px;height:34px;background:#8a8a8a}
.foot-name{font-size:7.5px;line-height:8.5px;color:#8a8a8a;font-weight:600}
.copy{position:absolute;left:56px;top:59px;font-size:8.5px;color:#aaa}
.connect{position:absolute;left:638px;top:36px;font-size:7.6px;font-weight:600;color:#ddd;letter-spacing:.2px}
.social{position:absolute;left:720px;top:30px;display:flex;gap:8.5px}
.social span{width:20px;height:20px;display:block;border-radius:2px}
</style>
</head>
<body>

<header>
  <div class="abs brand">
    <div class="brand-mark"></div>
    <div class="brand-name">Toll<br>For<br>Safer<br>Streets</div>
  </div>
  <div class="abs top-donate">MAKE A DONATION</div>
  <nav class="abs nav">
    <a class="current">HOME</a>
    <a>ABOUT TFSS</a>
    <a>ABOUT GUN VIOLENCE</a>
    <a>GET INVOLVED</a>
    <a>DONATE</a>
    <a>NEW &amp; EVENTS</a>
    <a>BLOG</a>
    <a>CONTACT TFSS</a>
  </nav>
</header>

<section class="abs hero">
  <div class="hero-photo" role="img" aria-label="Dark silhouette of a large bell hanging against a golden cloudy sunset sky"></div>
  <span class="qmark" style="left:462px;top:98px">“</span>
  <p class="quote">Turn out, pale lamps, to the pale sky,<br>The drifting cloud, the quiet light<br>The year is fading in the night..</p>
  <span class="qmark" style="left:820px;top:155px">”</span>
  <p class="author">- Lord Edmund Halvercombe</p>
  <svg class="arrows" width="50" height="24" viewBox="0 0 50 24">
    <polyline points="18,2 8,12 18,22" fill="none" stroke="#fff" stroke-width="2"/>
    <polyline points="32,2 42,12 32,22" fill="none" stroke="#d8174a" stroke-width="2"/>
  </svg>
</section>

<section class="abs donate-box">
  <h2 class="donate-title">MAKE A DONATION</h2>
  <p class="donate-sub">All your funds goes to New Gun Laws policies Campaign</p>
  <div class="donate-btn">DONATE NOW</div>
</section>

<article class="abs card" style="left:56px">
  <div class="card-img" role="img" aria-label="Black and white portrait of a young woman holding a sign reading Not One More" style="background:radial-gradient(ellipse 30% 60% at 55% 45%,#6a6a6a,#2a2a2a 70%),linear-gradient(90deg,#111,#333)"></div>
  <h3 class="card-title"><em>About</em> TFSS</h3>
  <p class="card-text">Lorem ipsum dolor sit amet, consectetur adipisicing eitseo eiusmod tempor incididunt ut labore et dolore magna aliqua. Sed ut perspiciatis unde omnis iste natus error sit voluptatem..</p>
  <a class="card-link">LEARN MORE</a>
</article>
<article class="abs card" style="left:329px">
  <div class="card-img" role="img" aria-label="Crowd of protesters with placards at an outdoor rally under a blue sky" style="background:linear-gradient(180deg,#5f8fd0 0%,#8fb0d8 22%,#5d7a3a 42%,#3f5a2a 58%,#7a3a44 76%,#2c3148 100%)"></div>
  <h3 class="card-title"><em>Get</em> INVOLVED</h3>
  <p class="card-text">Lorem ipsum dolor sit amet, consectetur adipisicing eitseo eiusmod tempor incididunt ut labore et dolore magna aliqua. Sed ut perspiciatis unde omnis iste natus error sit voluptatem..</p>
  <a class="card-link">LEARN MORE</a>
</article>
<article class="abs card" style="left:604px">
  <div class="card-img" role="img" aria-label="Banquet hall filled with guests seated at round tables under chandeliers" style="background:linear-gradient(180deg,#1c2440 0%,#3a3a5a 25%,#8a4a2e 55%,#c07a4e 80%,#6a2a1e 100%)"></div>
  <h3 class="card-title"><em>EVENTS</em> AT TFSS</h3>
  <p class="card-text">Lorem ipsum dolor sit amet, consectetur adipisicing eitseo eiusmod tempor incididunt ut labore et dolore magna aliqua. Sed ut perspiciatis unde omnis iste natus error sit voluptatem..</p>
  <a class="card-link">LEARN MORE</a>
</article>

<div class="abs rule"></div>
<h2 class="abs blog-head"><em>Latest From the</em> BLOG</h2>

<article class="abs post" style="left:56px">
  <div class="post-img" role="img" aria-label="Colourful protest signs at a gun control vigil" style="background:linear-gradient(120deg,#3e5f8a 0%,#e8c23a 35%,#e0603a 60%,#c21f3a 85%,#f0e6d8 100%)"></div>
  <h4 class="post-title">Veritatis et quasi architecto beatae</h4>
  <p class="post-date">Posted on 04, 2014</p>
  <p class="post-text">Lorem ipsum dolor sit amet, consectetur adipisicing eitseo eiusmod tempor incididunt ut labore et dolore magna aliqua.</p>
</article>
<article class="abs post" style="left:260px">
  <div class="post-img" role="img" aria-label="Marchers with flags and banners at a street demonstration" style="background:linear-gradient(180deg,#7aa2d6 0%,#4e7a3c 40%,#c8242e 65%,#2a3060 100%)"></div>
  <h4 class="post-title">Veritatis et quasi architecto beatae</h4>
  <p class="post-date">Posted on 04, 2014</p>
  <p class="post-text">Lorem ipsum dolor sit amet, consectetur adipisicing eitseo eiusmod tempor incididunt ut labore et dolore magna aliqua.</p>
</article>
<article class="abs post" style="left:466px">
  <div class="post-img" role="img" aria-label="Close-up of a revolver barrel pointed at the viewer" style="background:radial-gradient(circle at 38% 52%,#111 0 14%,#555 24%,#b89a98 45%,#e2c8c6 75%,#8a7a7a 100%)"></div>
  <h4 class="post-title">Veritatis et quasi architecto beatae</h4>
  <p class="post-date">Posted on 04, 2014</p>
  <p class="post-text">Lorem ipsum dolor sit amet, consectetur adipisicing eitseo eiusmod tempor incididunt ut labore et dolore magna aliqua.</p>
</article>
<article class="abs post" style="left:670px">
  <div class="post-img" role="img" aria-label="Activists lying on a plaza floor in a die-in protest" style="background:linear-gradient(160deg,#3a3632 0%,#8e8880 35%,#b8b0a4 55%,#6a4a3a 75%,#2e2a28 100%)"></div>
  <h4 class="post-title">Veritatis et quasi architecto beatae</h4>
  <p class="post-date">Posted on 04, 2014</p>
  <p class="post-text">Lorem ipsum dolor sit amet, consectetur adipisicing eitseo eiusmod tempor incididunt ut labore et dolore magna aliqua.</p>
</article>

<footer class="abs footer">
  <div class="foot-brand">
    <div class="foot-mark"></div>
    <div class="foot-name">Toll<br>For<br>Safer<br>Streets</div>
  </div>
  <p class="copy">Copyright @2014. All Right Reserved</p>
  <p class="connect">STAY CONNECTED</p>
  <div class="social" aria-label="Social links">
    <span style="background:#3b5998"></span>
    <span style="background:#1da1f2"></span>
    <span style="background:#cb2027"></span>
    <span style="background:#dd4b39"></span>
    <span style="background:#cd201f"></span>
  </div>
</footer>

</body>
</html>
```